Design of two graphics from basic existing design & colours

I have two graphics which I currently use but they are nothing special. We would like to transform these two graphics, using our existing logo colour, into something special. The outputs will be used:

- on our website;
- in a powerpoint sales presentation;
- in email campaigns; and
- to print for handing to prospects at the end of a sales presentation.

Please just submit one of the graphics and if we like the design, we will ask you to work on the second graphic. These two graphics are critical to our marketing and will be used together so we need them to have a similar look and feel.

```html
<!DOCTYPE html>
<html lang="en">
<head>
<meta charset="utf-8">
<title>Advisory Board Framework</title>
<link rel="stylesheet" href="https://fonts.googleapis.com/css2?family=Source+Sans+3:wght@600;700&display=swap">
<style>
  :root {
    --grey: #a3a3a3;
    --charcoal: #3b393a;
    --maroon: #67231c;
    --red: #d8302c;
    --black: #1b1b1b;
    --white: #ffffff;
    --ink: #222222;
    --list: #f1ecec;
  }
  html, body {
    margin: 0;
    padding: 0;
    overflow: hidden;
    background: var(--white);
  }
  .canvas {
    position: relative;
    width: 1200px;
    height: 1000px;
    overflow: hidden;
    background: var(--white);
    font-family: "Source Sans 3", sans-serif;
  }
  .canvas svg { position: absolute; left: 0; top: 0; }
  .segment-label {
    fill: var(--white);
    font-size: 11.5px;
    font-weight: 700;
    text-anchor: middle;
  }
  .cycle-caption {
    fill: var(--ink);
    font-size: 13px;
    font-weight: 700;
    text-anchor: middle;
  }
  .board-title {
    fill: var(--white);
    font-size: 16px;
    font-weight: 700;
    text-anchor: middle;
    letter-spacing: 0.3px;
  }
  .pillar-title {
    fill: var(--white);
    font-size: 13.5px;
    font-weight: 700;
    text-anchor: middle;
  }
  .pillar-list {
    fill: var(--list);
    font-size: 13.5px;
    font-weight: 600;
    text-anchor: middle;
  }
  .grey    { fill: var(--grey); }
  .charcoal{ fill: var(--charcoal); }
  .maroon  { fill: var(--maroon); }
  .red     { fill: var(--red); }
  .black   { fill: var(--black); }
  .segment.grey    { stroke: var(--grey); }
  .segment.charcoal{ stroke: var(--charcoal); }
  .segment.red     { stroke: var(--red); }
  .segment.black   { stroke: var(--black); }
  .segment { stroke-width: 10; stroke-linejoin: round; }
</style>
</head>
<body>
<div class="canvas">

  <svg class="framework" width="1200" height="1000" viewBox="0 0 1200 1000">
    <defs>
      <path id="seg" d="M -52,-184 A 191 191 0 0 1 52,-184 L 34,-124 A 129 129 0 0 0 -34,-124 Z"/>
      <g id="column">
        <path class="column-capital" d="M -81,533 H 81 C 81,549 74,558 60,560 H -60 C -74,558 -81,549 -81,533 Z"/>
        <rect class="column-necking" x="-66" y="564" width="132" height="8" rx="3"/>
        <rect class="column-shaft-head" x="-53" y="578" width="106" height="72"/>
        <rect class="column-shaft" x="-53" y="657" width="106" height="215"/>
        <rect class="column-ring" x="-53" y="878" width="106" height="7"/>
        <rect class="column-plinth" x="-66" y="890" width="132" height="12" rx="5"/>
        <path class="column-base" d="M -60,906 H 60 C 74,908 81,918 81,932 H -81 C -81,918 -74,908 -60,906 Z"/>
      </g>
    </defs>

    <!-- Management cycle wheel -->
    <line x1="663" y1="266" x2="1138" y2="266" stroke="var(--maroon)" stroke-width="2"/>
    <g class="cycle" transform="translate(900,266)">
      <g transform="rotate(0)"><use href="#seg" class="segment red"/>
        <text class="segment-label" y="-160"><tspan x="0">Strategic</tspan><tspan x="0" dy="12">Plan</tspan></text></g>
      <g transform="rotate(36)"><use href="#seg" class="segment black"/>
        <text class="segment-label" y="-166"><tspan x="0">Annual</tspan><tspan x="0" dy="12">Business</tspan><tspan x="0" dy="12">Plan</tspan></text></g>
      <g transform="rotate(72)"><use href="#seg" class="segment grey"/>
        <text class="segment-label" y="-160"><tspan x="0">Departmental</tspan><tspan x="0" dy="12">Plan</tspan></text></g>
      <g transform="rotate(108)"><use href="#seg" class="segment red"/>
        <text class="segment-label" transform="rotate(180 0 -160)" y="-176"><tspan x="0">Annual</tspan><tspan x="0" dy="11">Performance</tspan><tspan x="0" dy="11">Objectives</tspan><tspan x="0" dy="11">&amp; KPI's</tspan></text></g>
      <g transform="rotate(144)"><use href="#seg" class="segment charcoal"/>
        <text class="segment-label" transform="rotate(180 0 -160)" y="-166"><tspan x="0">Monthly</tspan><tspan x="0" dy="12">Performance</tspan><tspan x="0" dy="12">Meetings</tspan></text></g>
      <g transform="rotate(180)"><use href="#seg" class="segment red"/>
        <text class="segment-label" transform="rotate(180 0 -160)" y="-166"><tspan x="0">Individual</tspan><tspan x="0" dy="12">Performance</tspan><tspan x="0" dy="12">Plan</tspan></text></g>
      <g transform="rotate(216)"><use href="#seg" class="segment black"/>
        <text class="segment-label" transform="rotate(180 0 -160)" y="-166"><tspan x="0">Individual</tspan><tspan x="0" dy="12">Development</tspan><tspan x="0" dy="12">Plan</tspan></text></g>
      <g transform="rotate(252)"><use href="#seg" class="segment grey"/>
        <text class="segment-label" transform="rotate(180 0 -160)" y="-160"><tspan x="0">Succession</tspan><tspan x="0" dy="12">Plan</tspan></text></g>
      <g transform="rotate(288)"><use href="#seg" class="segment red"/>
        <text class="segment-label" y="-160"><tspan x="0">Business</tspan><tspan x="0" dy="12">Reviews</tspan></text></g>
      <g transform="rotate(324)"><use href="#seg" class="segment charcoal"/>
        <text class="segment-label" y="-166"><tspan x="0">Advisory</tspan><tspan x="0" dy="12">Board</tspan><tspan x="0" dy="12">Meetings</tspan></text></g>

      <circle class="cycle-ring" r="105" fill="none" stroke="var(--black)" stroke-width="2.5"/>
      <g class="cycle-arrows" fill="var(--black)">
        <path transform="rotate(-40)" d="M -5,-111 L 7,-105 L -5,-99 Z"/>
        <path transform="rotate(0)" d="M -5,-111 L 7,-105 L -5,-99 Z"/>
        <path transform="rotate(40)" d="M -5,-111 L 7,-105 L -5,-99 Z"/>
        <path transform="rotate(80)" d="M -5,-111 L 7,-105 L -5,-99 Z"/>
        <path transform="rotate(115)" d="M -5,-111 L 7,-105 L -5,-99 Z"/>
        <path transform="rotate(150)" d="M -5,-111 L 7,-105 L -5,-99 Z"/>
        <path transform="rotate(210)" d="M -5,-111 L 7,-105 L -5,-99 Z"/>
        <path transform="rotate(245)" d="M -5,-111 L 7,-105 L -5,-99 Z"/>
        <path transform="rotate(280)" d="M -5,-111 L 7,-105 L -5,-99 Z"/>
        <path transform="rotate(320)" d="M -5,-111 L 7,-105 L -5,-99 Z"/>
      </g>
      <text class="cycle-caption" y="-34">Managing Structure</text>
      <rect x="-80" y="-21" width="160" height="42" rx="3" class="maroon"/>
      <text class="board-title" y="6">ADVISORY BOARD</text>
      <text class="cycle-caption" y="40">Managing Performance</text>
    </g>

    <!-- Temple of four pillars -->
    <g class="temple">
      <path class="roof black" d="M 30,512 L 460,423 L 888,512 Z"/>
      <rect class="black" x="30" y="512" width="858" height="16"/>
      <rect class="black" x="30" y="938" width="858" height="14"/>

      <!-- Cultural pillar -->
      <g class="pillar" transform="translate(151,0)">
        <use href="#column" class="grey"/>
        <g class="icon-people" fill="var(--white)">
          <circle cx="0" cy="597" r="4"/><path d="M -6,609 Q 0,601 6,609 Z"/>
          <circle cx="-13" cy="609" r="4"/><path d="M -19,621 Q -13,613 -7,621 Z"/>
          <circle cx="13" cy="609" r="4"/><path d="M 7,621 Q 13,613 19,621 Z"/>
          <path d="M 0,605 V 611 M 0,611 L -7,615 M 0,611 L 7,615" stroke="var(--white)" stroke-width="1.2"/>
        </g>
        <text class="pillar-title" y="647">CULTURAL</text>
        <text class="pillar-list" y="694">
          <tspan x="0">Coaching</tspan><tspan x="0" dy="17">Communication</tspan><tspan x="0" dy="17">Competencies</tspan><tspan x="0" dy="17">Development</tspan><tspan x="0" dy="17">Employment</tspan><tspan x="0" dy="17">Leadership</tspan><tspan x="0" dy="17">Performance</tspan><tspan x="0" dy="17">Profiles</tspan><tspan x="0" dy="17">Succession</tspan><tspan x="0" dy="17">Teams</tspan>
        </text>
      </g>

      <!-- Strategic pillar -->
      <g class="pillar" transform="translate(356,0)">
        <use href="#column" class="charcoal"/>
        <g class="icon-chart" fill="var(--white)">
          <path d="M -17,588 V 623 H 18" fill="none" stroke="var(--white)" stroke-width="1.5"/>
          <rect x="-12" y="613" width="5" height="9"/><rect x="-4" y="607" width="5" height="15"/>
          <rect x="4" y="610" width="5" height="12"/><rect x="12" y="600" width="5" height="22"/>
          <path d="M -13,606 L -4,598 L 4,603 L 16,591" fill="none" stroke="var(--white)" stroke-width="1.3"/>
        </g>
        <text class="pillar-title" y="647">STRATEGIC</text>
        <text class="pillar-list" y="694">
          <tspan x="0">Board</tspan><tspan x="0" dy="17">Purpose</tspan><tspan x="0" dy="17">Risk</tspan><tspan x="0" dy="17">Strategy</tspan><tspan x="0" dy="17">Structure</tspan><tspan x="0" dy="17">Values</tspan><tspan x="0" dy="17">Vision</tspan>
        </text>
      </g>

      <!-- Operational pillar -->
      <g class="pillar" transform="translate(561,0)">
        <use href="#column" class="maroon"/>
        <g class="icon-gears">
          <circle cx="6" cy="604" r="10" fill="none" stroke="var(--white)" stroke-width="5" stroke-dasharray="3.5 2.8"/>
          <circle cx="6" cy="604" r="8" fill="var(--white)"/><circle cx="6" cy="604" r="3.5" class="maroon"/>
          <circle cx="-15" cy="614" r="6" fill="none" stroke="var(--white)" stroke-width="3.5" stroke-dasharray="2.5 2"/>
          <circle cx="-15" cy="614" r="5" fill="var(--white)"/><circle cx="-15" cy="614" r="2" class="maroon"/>
        </g>
        <text class="pillar-title" y="647">OPERATIONAL</text>
        <text class="pillar-list" y="694">
          <tspan x="0">Competitor</tspan><tspan x="0" dy="17">Compliance</tspan><tspan x="0" dy="17">Customer</tspan><tspan x="0" dy="17">Marketing</tspan><tspan x="0" dy="17">Meetings</tspan><tspan x="0" dy="17">Planning</tspan><tspan x="0" dy="17">Policy</tspan><tspan x="0" dy="17">Projects</tspan><tspan x="0" dy="17">Reporting</tspan><tspan x="0" dy="17">Review</tspan>
        </text>
      </g>

      <!-- Financial pillar -->
      <g class="pillar" transform="translate(766,0)">
        <use href="#column" class="red"/>
        <text class="pillar-title" y="622" style="font-size:34px;font-weight:600">$</text>
        <text class="pillar-title" y="647">FINANCIAL</text>
        <text class="pillar-list" y="694">
          <tspan x="0">Budget</tspan><tspan x="0" dy="17">CAPEX</tspan><tspan x="0" dy="17">Cash Flow</tspan><tspan x="0" dy="17">Delegations</tspan><tspan x="0" dy="17">OPEX</tspan>
        </text>
      </g>
    </g>
  </svg>
</div>
</body>
</html>
```